Flyer for "Master the Mash Tun Basics" course

NEEDED: A6 flyer designed to advertise my first training course:
Intro to craft beer brewing

The company brand identity was recently bought from Pixel Harbor and it can be seen, with colour scheme on our website: www.TinmoorKettle.com.

The flyer is to be in line with my current brand identity and have a strong hook to push people to our site.

The flyer's goal is to get people to visit the site to book on a craft beer brewing training course. The info available to be included, although you have the freedom to include as much or as little as you see fit:

Currently a sale of 60% off on the course cost
RRP £120 Sale Price £50 (limited time only)
Courses will be run in central London
The website is TinmoorKettle.com
Hands on, half day course, brunch and a couple of sample beers included
Dates available:
14th December 2014
11th January 2015
18th January 2015
25th January 2015
1st February 2015
8th February 2015
15th February 2015
22nd February 2015

Logo file included, AI version available on request. Any photo on the TinmoorKettle.com site is available to be used. Simply pull of the site or I can send to you.

Colour scheme used on site: #FF9700 & #26210D

I will reply to any designs offered between 8pm and 11pm BST each day.

Good luch!

Hi everyone, We have now reviewed the first submissions and there are some ok, some good and a couple of great efforts in there. Here are the following common things that we commented on in our first reviews: 1. WHAT IS THE FLYER TRYING TO SAY... YOU'VE GOT 1 SECOND!!!! This flyer is to be given out in the street. That gives you 1second to tell the reader what the flyer is selling. That is the number 1 priority for the flyer. Please make it your priority as designers. 2. SALE SALE SALE This is the number 2 priority, people love SALES and a big colourful sticker saying SALE or 60% OFF (or both) is to be positioned so once the reader has seen that the flyer is about a craft beer brewing course, they see there is a sale on the course. 3. BRAND PERSONALITY 3rd priority is the Tinmoor Kettle brand identity. We picked this name, logo and colour scheme to stand out. Please use these to enhance points 1 & 2, but also get our logo on there is a bold and brash way. 4. USE THE BACK OF THE CARD Place any info that is not required in 1, 2 & 3 on the back, or even remove it all together if YOU feel it is not suited. You are the designer, so make some design decisions! We are happy to ask you to add things back in if we feel it is lacking. Our best guess (and we are NOT designers) is that putting either the dates OR a brief description of the course on the back would be enough info. If you think we can get bother, without overloading the page, give it a go! 5. CALL TO ACTION On the front and on the back, we want a CALL TO ACTION. Book at TinmoorKettle.com or just TinmoorKettle.com (you do not need http://www before it!!! We live in 2014 not 1994!!!) 6. MAKE IT BOLD, & THEN MAKE IT BOLDER This flyer is to stand out to a person that is handed 1 different leaflet every 2 minutes while walking down a busy London high street. We MUST stand out. Finally, thanks for all the designer so far, your efforts are greatly appreciated and we are very excited about the new revision of the design!

Target Market(s)

City living, young professionals who like to do fun things at the weekend.

Industry/Entity Type

Training

Font styles to use
Sans Serif

Colors
f78f20

Requirements
Must have
• Strong brand identity and call to action
In line with brand identity, see website www.TinmoorKettle.com

```html
<!DOCTYPE html>
<html lang="en">
<head>
<meta charset="utf-8">
<title>Intro to Craft Beer Brewing – Tinmoor Kettle Flyer</title>
<link rel="stylesheet" href="https://fonts.googleapis.com/css2?family=Arimo:wght@400;700&display=swap">
<style>
  :root {
    --page-bg: #e6e6e4;
    --panel-dark: #3a3937;
    --brand-orange: #e39a00;
    --accent-orange: #f0a21a;
    --ink: #111111;
    --white: #ffffff;
    --beer-light: #f4c45a;
    --beer-mid: #e0a024;
    --beer-deep: #b8740c;
    --foam: #f3eee2;
  }
  * { box-sizing: border-box; margin: 0; padding: 0; }
  html, body {
    width: 1200px;
    height: 1000px;
    overflow: hidden;
    background: var(--page-bg);
    font-family: "Arimo", Arial, sans-serif;
  }
  .flyer {
    position: absolute;
    left: 40px;
    top: 102px;
    width: 1120px;
    height: 795px;
    overflow: hidden;
    background: var(--panel-dark);
  }
  .beer-photo {
    position: absolute;
    left: 321px;
    top: 0;
    width: 799px;
    height: 795px;
    background:
      radial-gradient(ellipse at 70% 60%, rgba(255,220,130,0.35), transparent 55%),
      linear-gradient(180deg, var(--foam) 0%, #efe0b8 7%, var(--beer-light) 15%, var(--beer-mid) 50%, var(--beer-deep) 100%);
  }
  .side-panel {
    position: absolute;
    left: 0;
    top: 0;
    width: 321px;
    height: 795px;
    background: var(--panel-dark);
  }
  .brand-mark {
    position: absolute;
    left: 22px;
    top: 240px;
    width: 270px;
    display: flex;
    align-items: center;
    gap: 14px;
    color: var(--accent-orange);
    font-weight: 700;
    font-size: 38px;
    line-height: 1.05;
  }
  .brand-mark__dot {
    flex: 0 0 34px;
    height: 34px;
    border-radius: 50%;
    background: var(--accent-orange);
  }
  .sale {
    position: absolute;
    left: 24px;
    top: 560px;
    display: flex;
    align-items: flex-start;
    font-weight: 700;
    line-height: 1;
  }
  .sale__number { font-size: 112px; color: var(--white); letter-spacing: -3px; }
  .sale__unit { display: flex; flex-direction: column; margin-left: 2px; margin-top: 4px; }
  .sale__percent { font-size: 54px; color: var(--white); }
  .sale__off { font-size: 54px; color: var(--accent-orange); margin-top: -4px; }
  .cta-band {
    position: absolute;
    left: 0;
    top: 669px;
    width: 1120px;
    height: 79px;
    background: var(--brand-orange);
  }
  .cta-band__course {
    position: absolute;
    left: 34px;
    top: 4px;
    font-size: 70px;
    font-weight: 700;
    color: var(--ink);
    line-height: 1;
  }
  .cta-band__url {
    position: absolute;
    left: 321px;
    width: 799px;
    top: 22px;
    text-align: center;
    font-size: 36px;
    font-weight: 700;
    color: var(--white);
    letter-spacing: 0.5px;
  }
  .headline {
    position: absolute;
    left: 321px;
    width: 799px;
    top: 190px;
    text-align: center;
    color: var(--white);
    font-weight: 700;
    text-shadow: 0 2px 8px rgba(90,50,0,0.35);
  }
  .headline__intro {
    display: flex;
    align-items: center;
    justify-content: center;
    gap: 14px;
    font-size: 32px;
    color: var(--ink);
    text-shadow: none;
    font-weight: 400;
  }
  .headline__intro::before,
  .headline__intro::after {
    content: "";
    width: 210px;
    height: 2px;
    background: var(--white);
  }
  .headline__main { font-size: 100px; line-height: 1; letter-spacing: -1px; margin-top: 8px; }
  .headline__sub { font-size: 100px; line-height: 1; margin-top: 6px; }
  .more-info {
    position: absolute;
    left: 321px;
    width: 799px;
    top: 600px;
    text-align: center;
    font-size: 52px;
    font-weight: 700;
    color: var(--ink);
  }
</style>
</head>
<body>
  <main class="flyer">
    <div class="beer-photo" role="img" aria-label="Close-up photograph of golden beer with rising bubbles and white foam at the top"></div>
    <aside class="side-panel">
      <div class="brand-mark">
        <span class="brand-mark__dot"></span>
        <span class="brand-mark__name">Tinmoor Kettle</span>
      </div>
      <div class="sale">
        <span class="sale__number">60</span>
        <span class="sale__unit">
          <span class="sale__percent">%</span>
          <span class="sale__off">off</span>
        </span>
      </div>
    </aside>
    <section class="headline">
      <p class="headline__intro">Intro to</p>
      <h1 class="headline__main">Craft Beer</h1>
      <p class="headline__sub">BREWING</p>
    </section>
    <p class="more-info">+info</p>
    <div class="cta-band">
      <span class="cta-band__course">course</span>
      <span class="cta-band__url">www.TinmoorKettle.com</span>
    </div>
  </main>
</body>
</html>
```